Venture firm needs flyer to attract Sales Professionals as Advisors

Creation of either a pdf Flyer or Brochure.
The target audience are senior sales professionals of the Information Technology industry. The flyer needs to come across highly professional, business oriented, positive. Text for the brochure is attached. The colors/graphics should align with Brindmore Capital corporate appearance: www.brindmore.capital

Target Market(s)

Sales Professionals in the Information Technology Industry

Industry/Entity Type

Information Technology

Font styles to use
• Raleway

Requirements
Must have
• fitting the corporate look and feel: www.brindmore.capital

```html
<!DOCTYPE html>
<html lang="en">
<head>
<meta charset="utf-8">
<title>Brindmore Sales Council</title>
<link href="https://fonts.googleapis.com/css2?family=Open+Sans:wght@800&family=Raleway:wght@200;300&display=swap" rel="stylesheet">
<style>
  :root {
    --sky-top: #333a4a;
    --sky-mid: #7888a0;
    --ridge: #3b3a55;
    --slope: #3a2438;
    --valley: #221f2f;
    --base: #1b1c28;
    --ink-light: #ffffff;
    --ink-body: #eceef5;
    --ink-muted: #c9cde0;
    --frame: #4a4f6a;
  }
  * { margin: 0; padding: 0; box-sizing: border-box; }
  html, body { width: 850px; height: 1200px; overflow: hidden; background: var(--base); }
  .flyer {
    position: relative;
    width: 850px;
    height: 1200px;
    overflow: hidden;
  }
  .backdrop {
    position: absolute;
    inset: 0;
    background:
      radial-gradient(ellipse 70% 25% at 75% 52%, rgba(140, 30, 60, 0.45), transparent 70%),
      linear-gradient(180deg,
        var(--sky-top) 0%,
        var(--sky-mid) 26%,
        var(--ridge) 34%,
        var(--slope) 50%,
        var(--valley) 68%,
        var(--base) 100%);
  }
  .title {
    position: absolute;
    top: 80px;
    right: 62px;
    text-align: right;
    font-family: "Open Sans", sans-serif;
    font-weight: 800;
    font-size: 76px;
    line-height: 90px;
    letter-spacing: 2px;
    color: var(--ink-light);
    text-transform: uppercase;
  }
  .title span { display: block; }
  .title .title-first { margin-right: 18px; }
  .intro {
    position: absolute;
    top: 464px;
    left: 92px;
    width: 668px;
    font-family: "Raleway", sans-serif;
    font-weight: 300;
    font-size: 19.5px;
    line-height: 41.5px;
    letter-spacing: 1px;
    color: var(--ink-body);
  }
  .intro p {
    text-align: justify;
    text-align-last: center;
    margin-bottom: 40px;
  }
  .brand-tag {
    position: absolute;
    left: 65px;
    top: 1093px;
    width: 326px;
    height: 54px;
    border: 1px solid var(--frame);
    display: flex;
    align-items: center;
    justify-content: center;
    font-family: "Raleway", sans-serif;
    font-weight: 200;
    font-size: 27px;
    letter-spacing: 0.5px;
    color: var(--ink-muted);
    text-transform: uppercase;
  }
</style>
</head>
<body>
  <main class="flyer">
    <div class="backdrop" role="img" aria-label="Photograph of a rugged mountain range at dusk under a blue-grey sky, with snow patches and red-lit slopes fading into darkness"></div>

    <h1 class="title">
      <span class="title-first">Brindmore</span>
      <span class="title-second">Sales Council</span>
    </h1>

    <section class="intro">
      <p>The BSC is a by invitation only global community of high caliber Sales Professionals in the IT industry. Participating in the BSC provides significant wealth creation opportunities by earning consulting fees and sales commission or finding an exciting startup to work for.</p>
      <p>BSC members actively collaborate with each other to close deals, generate leads &amp; opportunities, navigate through client organizations and build a true advisory status with customers.</p>
      <p>BSC members get early first hand visibility into the latest technology innovations and learn how those technologies could assist their clients in solving their complex business objectives.</p>
    </section>

    <div class="brand-tag">Brindmore Capital</div>
  </main>
</body>
</html>
```